Startup Technology Consulting Firm in NYC Needs A Website

I need a website built for my startup technology consulting company Brightmoor Systems Collective. We offer a unique white glove service that provides end to end technology support. I want to stand out above the rest. We are small firm but are very dedicated which where we derive our name from BSC primarily offers
end to end technology advisory services to small businesses lacking their own IT staff. We offer top notch white glove and our customer service and satisfaction is exceed by no one.

Below are some of what we provide our clients

Strategic IT Planning
Business Continuity Planning/Disaster Recovery
Cloud Computing\DataCenter Solutions
Server Infrastructure/Networking
Virtualization Technologies
Project Management

Our Technology Advisors hold many certifications from Quillora & Tessfold. We are also Quillora Partners

I have attached my logo (preview design) As soon as I ge the final images I will upload.

Reason: want to give more time to submit designs

Industry/Entity Type

Information Technology

Coding

Coded - Design and coding required

Number of Pages Required

1 page

Font styles to use
Sans Serif

Requirements
Must have
• Attract Target Market. The site should bleed the company vision
• DEDICATION everything about the site should show this
• Layout the Benefits of our offerings
• Links to my social media
• Links to dircct my client's for remote support

```html
<!DOCTYPE html>
<html lang="en">
<head>
<meta charset="utf-8">
<title>Brightmoor Systems Collective</title>
<link href="https://fonts.googleapis.com/css2?family=Open+Sans:wght@300;400;600;700&family=Roboto:wght@400;500&display=swap" rel="stylesheet">
<style>
  :root {
    --brand-blue: #0d3a8c;
    --footer-blue: #0b2f8e;
    --chip-blue: #1a47a8;
    --ink: #333333;
    --body-ink: #555555;
    --rule: #e3e3e3;
    --white: #ffffff;
    --partner-grey: #6b6b6b;
  }
  * { box-sizing: border-box; margin: 0; padding: 0; }
  html, body { width: 888px; height: 1200px; overflow: hidden; background: var(--white); }
  body { position: relative; font-family: "Roboto", sans-serif; color: var(--ink); }

  .site-header { position: absolute; left: 0; top: 0; width: 888px; height: 108px; }
  .brand { position: absolute; left: 112px; top: 8px; width: 165px; text-align: center; }
  .brand-mark { display: block; width: 46px; height: 46px; margin: 0 auto 8px; border-radius: 50%; background: #9cc4e4; }
  .brand-name { font-family: "Open Sans", sans-serif; font-weight: 600; font-size: 11.5px; line-height: 14px; letter-spacing: 0.6px; color: var(--brand-blue); text-transform: uppercase; }

  .partners { position: absolute; right: 112px; top: 22px; display: flex; align-items: center; gap: 22px; font-family: "Open Sans", sans-serif; font-size: 14px; color: var(--partner-grey); }
  .partner { display: flex; align-items: center; gap: 5px; }
  .partner-square { width: 16px; height: 16px; background: #8a8a8a; }

  .main-nav { position: absolute; top: 65px; left: 391px; display: flex; font-family: "Open Sans", sans-serif; font-size: 11px; color: #222; }
  .main-nav a { color: inherit; text-decoration: none; height: 25px; line-height: 23px; }
  .main-nav .home { width: 47px; text-align: center; border: 1.5px solid var(--brand-blue); color: var(--brand-blue); border-radius: 2px; }
  .nav-about { position: absolute; left: 66px; }
  .nav-services { position: absolute; left: 142px; }
  .nav-features { position: absolute; left: 213px; }
  .nav-blog { position: absolute; left: 285px; }
  .nav-contact { position: absolute; left: 332px; white-space: nowrap; }

  .hero { position: absolute; left: 0; top: 108px; width: 888px; height: 402px;
    background: linear-gradient(180deg, #0e2f8a 0%, #1a4aa0 38%, #3b5f9a 58%, #8a6a4a 70%, #c78a3c 76%, #23355e 84%, #1a2b55 100%); }
  .hero-headline { position: absolute; left: 466px; top: 50px; width: 300px; text-align: center; font-family: "Open Sans", sans-serif; font-weight: 300; font-size: 22px; line-height: 27.5px; color: var(--white); }
  .hero-dots { position: absolute; left: 390px; top: 359px; display: flex; gap: 11px; }
  .hero-dots span { width: 13px; height: 13px; border: 1.5px solid var(--white); border-radius: 50%; }
  .hero-dots .active { background: var(--white); }

  .section-title { position: absolute; left: 0; width: 888px; text-align: center; font-family: "Open Sans", sans-serif; font-weight: 700; font-size: 15.5px; color: var(--brand-blue); }
  .title-rule { position: absolute; left: 412px; width: 64px; height: 1.5px; background: #7f9ac9; }

  .welcome-text { position: absolute; left: 144px; top: 580px; width: 600px; text-align: center; font-size: 10.2px; line-height: 17.8px; color: var(--body-ink); }
  .read-more { position: absolute; left: 0; top: 648px; width: 888px; text-align: center; font-family: "Open Sans", sans-serif; font-weight: 700; font-size: 9.6px; letter-spacing: 1.2px; color: var(--brand-blue); }
  .read-more .caret { display: inline-block; margin-left: 6px; border-left: 4px solid var(--brand-blue); border-top: 3.5px solid transparent; border-bottom: 3.5px solid transparent; vertical-align: 1px; }

  .hrule { position: absolute; left: 112px; width: 664px; height: 1.5px; background: var(--rule); }
  .vrule { position: absolute; width: 1px; background: var(--rule); }

  .service { position: absolute; width: 210px; text-align: center; }
  .service svg { display: block; margin: 0 auto; }
  .service-name { font-family: "Open Sans", sans-serif; font-weight: 600; font-size: 12.2px; line-height: 15.5px; color: #2b2b2b; }
  .service-text { margin-top: 6px; font-size: 9.6px; line-height: 15.5px; color: #444; }

  .site-footer { position: absolute; left: 0; top: 1090px; width: 888px; height: 110px; background: var(--footer-blue); color: var(--white); }
  .follow-label { position: absolute; left: 112px; top: 27px; font-size: 10px; }
  .social { position: absolute; left: 110px; top: 50px; display: flex; gap: 4px; }
  .social a { width: 25px; height: 25px; border-radius: 50%; background: var(--chip-blue); display: block; }
  .footer-nav { position: absolute; right: 112px; top: 33px; font-size: 9.6px; }
  .footer-nav span { margin: 0 6px; }
  .copyright { position: absolute; right: 112px; top: 57px; font-size: 9.6px; }
</style>
</head>
<body>

<header class="site-header">
  <div class="brand">
    <span class="brand-mark"></span>
    <div class="brand-name">Brightmoor Systems Collective</div>
  </div>
  <div class="partners">
    <div class="partner"><span class="partner-square"></span>Quillora</div>
    <div class="partner">Tessfold</div>
  </div>
  <nav class="main-nav">
    <a class="home" href="#">Home</a>
    <a class="nav-about" href="#">About Us</a>
    <a class="nav-services" href="#">Services</a>
    <a class="nav-features" href="#">Features</a>
    <a class="nav-blog" href="#">Blog</a>
    <a class="nav-contact" href="#">Contact Us</a>
  </nav>
</header>

<section class="hero" role="img" aria-label="Night city skyline with a suspension bridge lit over the river">
  <h1 class="hero-headline">We offer end to end technology advisory services to small businesses</h1>
  <div class="hero-dots"><span></span><span class="active"></span><span></span><span></span><span></span></div>
</section>

<h2 class="section-title" style="top:538px;">WELCOME TO OUR SITE</h2>
<div class="title-rule" style="top:563px;"></div>
<p class="welcome-text">There are many variations of passages of Lorem Ipsum available, but the majority have suffered alteration in some form, by injected humour, or randomised words which don't look even slightly believable. If you are going to use a passage of Lorem Ipsum, you need to be sure there isn't anything embarrassing hidden.</p>
<div class="read-more">READ MORE<span class="caret"></span></div>

<div class="hrule" style="top:687px;"></div>

<h2 class="section-title" style="top:715px;">OUR SERVICES</h2>
<div class="title-rule" style="top:741px;"></div>

<div class="vrule" style="left:323px; top:774px; height:118px;"></div>
<div class="vrule" style="left:568px; top:774px; height:118px;"></div>
<div class="hrule" style="top:912px;"></div>
<div class="vrule" style="left:323px; top:934px; height:120px;"></div>
<div class="vrule" style="left:568px; top:934px; height:120px;"></div>

<div class="service" style="left:94px; top:768px;">
  <svg width="34" height="48" viewBox="0 0 34 48" fill="none" stroke="#7a3fa8" stroke-width="1.6">
    <path d="M17 3a13 13 0 0 0-8 23c2 2 3 4 3 7h10c0-3 1-5 3-7A13 13 0 0 0 17 3z"/>
    <path d="M12 37h10M13 41h8M15 45h4"/>
  </svg>
  <div class="service-name" style="margin-top:11px;">Strategic IT Planning</div>
  <p class="service-text">Contrary to popular belief, Lorem Ipsum is not simply random text.</p>
</div>

<div class="service" style="left:339px; top:770px;">
  <svg width="58" height="42" viewBox="0 0 58 42" fill="none" stroke="#2f6fc0" stroke-width="1.8">
    <path d="M3 20l30 5-6 14L3 27z" fill="#cfe0f5"/>
    <path d="M8 24h16M10 28h14M12 32h12"/>
    <path d="M30 26L52 4l5 5-22 22-7 2z" fill="#7fb0e6"/>
  </svg>
  <div class="service-name" style="margin-top:14px;">Business Continuity Planning<br>/Disaster Recovery</div>
  <p class="service-text">Contrary to popular belief, Lorem Ipsum is not simply random text.</p>
</div>

<div class="service" style="left:581px; top:776px;">
  <svg width="56" height="36" viewBox="0 0 56 36" fill="none" stroke="#2a8f8a" stroke-width="2.4">
    <path d="M12 32a9 9 0 0 1 0-18 13 13 0 0 1 25-3 10 10 0 0 1 8 21z"/>
  </svg>
  <div class="service-name" style="margin-top:20px;">Cloud Computing\<br>DataCenter Solutions</div>
  <p class="service-text">Contrary to popular belief, Lorem Ipsum is not simply random text.</p>
</div>

<div class="service" style="left:94px; top:936px;">
  <svg width="40" height="44" viewBox="0 0 40 44">
    <g fill="#4d8a2e">
      <rect x="2" y="2" width="36" height="10" rx="1"/>
      <rect x="2" y="14" width="36" height="10" rx="1"/>
      <rect x="2" y="26" width="36" height="10" rx="1"/>
      <rect x="0" y="40" width="40" height="2"/>
    </g>
    <g fill="#ffffff"><rect x="6" y="5" width="8" height="4"/><rect x="6" y="17" width="8" height="4"/><rect x="6" y="29" width="8" height="4"/><circle cx="28" cy="7" r="1.2"/><circle cx="32" cy="7" r="1.2"/><circle cx="28" cy="19" r="1.2"/><circle cx="32" cy="19" r="1.2"/><circle cx="28" cy="31" r="1.2"/><circle cx="32" cy="31" r="1.2"/></g>
  </svg>
  <div class="service-name" style="margin-top:18px;">Server Infrastructure/Networking</div>
  <p class="service-text">Contrary to popular belief, Lorem Ipsum is not simply random text.</p>
</div>

<div class="service" style="left:339px; top:936px;">
  <svg width="44" height="44" viewBox="0 0 44 44" fill="none" stroke="#e8731c" stroke-width="2.4">
    <rect x="17" y="2" width="10" height="9"/><rect x="2" y="32" width="10" height="9"/><rect x="17" y="32" width="10" height="9"/><rect x="32" y="32" width="10" height="9"/>
    <path d="M22 11v10M7 32V21h30v11M22 21v11"/>
  </svg>
  <div class="service-name" style="margin-top:18px;">Virtualisation Technologies</div>
  <p class="service-text">Contrary to popular belief, Lorem Ipsum is not simply random text.</p>
</div>

<div class="service" style="left:581px; top:940px;">
  <svg width="66" height="40" viewBox="0 0 66 40">
    <g fill="#5a3b34"><circle cx="14" cy="14" r="7"/><circle cx="32" cy="10" r="8"/><rect x="2" y="26" width="26" height="13"/></g>
    <g fill="#9a8a86"><circle cx="50" cy="14" r="7"/><rect x="30" y="26" width="34" height="13"/></g>
    <g fill="#ffffff"><circle cx="14" cy="14" r="2.5"/><circle cx="32" cy="10" r="3"/><circle cx="50" cy="14" r="2.5"/></g>
  </svg>
  <div class="service-name" style="margin-top:18px;">Project Management</div>
  <p class="service-text">Contrary to popular belief, Lorem Ipsum is not simply random text.</p>
</div>

<footer class="site-footer">
  <div class="follow-label">Follow us on</div>
  <div class="social">
    <a href="#" aria-label="Social profile one"></a>
    <a href="#" aria-label="Social profile two"></a>
    <a href="#" aria-label="Social profile three"></a>
    <a href="#" aria-label="Social profile four"></a>
  </div>
  <nav class="footer-nav">Home<span>\</span>About Us<span>\</span>Services<span>\</span>Features<span>\</span>Blog<span>\</span>Contact Us</nav>
  <div class="copyright">Copyrights @&nbsp; 2015 All Rights Reserved</div>
</footer>

</body>
</html>
```